I sell Finches---picture of White Finch Bird----

I raise and sell light color and white Finch - need card to give to Pet shops with my name - Lorna Pettigrew, address: 271 North Ardmore Ln. Santa Barbara, Ca. 93187 - phone - 805-479-3816. All birds raised and nourished in large outside aviary--very healthy and cared for. Would like card to be shiny red with bold print in Broadway font----purple bold print on red card. Design options open - you know best. Would like a picture or pictures of Finches - light or white in color.

Industry/Entity Type

Pet

Contact Information for Business Card

THE WREN KEEPER (LARGE, BOLD BROADWAY PRINT)

```html
<!DOCTYPE html>
<html lang="en">
<head>
<meta charset="utf-8">
<title>The Wren Keeper – Business Card</title>
<link rel="stylesheet" href="https://fonts.googleapis.com/css2?family=Arimo:wght@400;700&family=Kanit:wght@600&family=Fira+Sans:wght@500&display=swap">
<style>
  :root {
    --page-bg: #e9e7e4;
    --card-bg: #ffffff;
    --brand-red: #e3262b;
    --band-red: #ea2328;
    --band-deep: #c9171c;
    --name-brown: #9a5b1f;
    --ink: #111111;
    --band-text: #ffffff;
    --photo-warm: #b39676;
    --photo-cool: #9a9891;
    --photo-light: #f1ede6;
  }
  * { box-sizing: border-box; margin: 0; padding: 0; }
  html, body {
    width: 1200px; height: 1200px; overflow: hidden;
    background: var(--page-bg);
  }
  .canvas {
    width: 1200px; height: 1200px;
    display: flex; align-items: center; justify-content: center;
  }
  .business-card {
    position: relative;
    width: 1080px; height: 617px;
    background: var(--card-bg);
    overflow: hidden;
    box-shadow: 0 6px 24px rgba(0,0,0,0.12);
  }
  .owner-name {
    position: absolute; left: 40px; top: 34px;
    font-family: "Arimo", sans-serif; font-size: 32px;
    color: var(--name-brown);
  }
  .business-title {
    position: absolute; right: 46px; top: 34px;
    font-family: "Kanit", sans-serif; font-weight: 600;
    font-size: 56px; letter-spacing: 2px; line-height: 1;
    color: var(--brand-red);
  }
  .contact-line {
    position: absolute; left: 40px;
    display: flex; align-items: center; gap: 12px;
    font-family: "Arimo", sans-serif; font-size: 27px;
    color: var(--ink);
  }
  .contact-line svg { width: 26px; height: 26px; flex: none; }
  .contact-address { top: 94px; }
  .contact-phone { top: 140px; }
  .finch-photo {
    position: absolute; left: 40px; top: 190px;
    width: 1010px; height: 290px;
    background:
      radial-gradient(ellipse 60% 55% at 50% 55%, rgba(179,150,118,0.55), rgba(179,150,118,0) 70%),
      linear-gradient(90deg, var(--photo-light) 0%, var(--photo-warm) 20%, var(--photo-cool) 50%, var(--photo-warm) 75%, var(--photo-light) 100%);
    border-radius: 6px;
    opacity: 0.85;
  }
  .tagline-band {
    position: absolute; left: 0; bottom: 0;
    width: 1080px; height: 190px;
  }
  .tagline {
    position: absolute; left: 0; right: 0; bottom: 48px;
    text-align: center;
    font-family: "Fira Sans", sans-serif; font-weight: 500;
    font-size: 27px; line-height: 1.3; letter-spacing: 0.5px;
    color: var(--band-text);
    transform: rotate(1.6deg);
  }
</style>
</head>
<body>
<main class="canvas">
  <section class="business-card">
    <p class="owner-name">Lorna Pettigrew</p>
    <h1 class="business-title">THE WREN KEEPER</h1>

    <p class="contact-line contact-address">
      <svg viewBox="0 0 24 24" aria-hidden="true"><path d="M12 3 1 12h3v9h6v-6h4v6h6v-9h3z" fill="var(--ink)"/><rect x="16" y="4" width="3" height="5" fill="var(--ink)"/></svg>
      271 North Ardmore Ln. Santa Barbara, Ca. 93187 -
    </p>
    <p class="contact-line contact-phone">
      <svg viewBox="0 0 24 24" aria-hidden="true"><path d="M3 8c0-3 4-5 9-5s9 2 9 5v2h-5V8c-1-1-7-1-8 0v2H3z" fill="var(--ink)"/><path d="M6 12h12l2 9H4z" fill="var(--ink)"/><circle cx="12" cy="16" r="2.5" fill="#fff"/></svg>
      805-479-3816.
    </p>

    <div class="finch-photo" role="img" aria-label="Photograph of six colourful finches perched in a row on a leafy branch"></div>

    <svg class="tagline-band" viewBox="0 0 1080 190" preserveAspectRatio="none" aria-hidden="true">
      <defs>
        <linearGradient id="bandShade" x1="0" y1="0" x2="0" y2="1">
          <stop offset="0" stop-color="var(--band-red)"/>
          <stop offset="1" stop-color="var(--band-deep)"/>
        </linearGradient>
      </defs>
      <path d="M0 190 L0 60 Q0 20 40 20 L1000 55 L1080 130 L1080 190 Z" fill="url(#bandShade)"/>
    </svg>
    <p class="tagline">ALL BIRDS RAISED AND NOURISHED IN LARGE OUTSIDE AVIARY<br>VERY HEALTHY AND CARED FOR.</p>
  </section>
</main>
</body>
</html>
```